Classy website for Corporate Entertainment - Action & Acrobatic Shows

12-Page Website to be coded using Wordpress!

We are "Velvet Summit Productions". We are all about providing 'experiences'! This website must be part of that experience :)

Please do not use our current website as inspiration for your design! We are looking for something new, and our business has outgrown that site (which was just for our shows) :)

We perform Action & Acrobatic Shows for corporate functions, as well as run Classes & Workshops from our Training Centre (Parkour, Acrobatics, etc), as well as Client Action Experiences and other services.

Example of our recent Morgan Vale 'Acrobatic Action Show' https://clipvault.example/watch/QxTr7nLpWzK

Our website must be super-classy/suave!! Needs to be heavily appealing to the Corporate community!

www.friendsphere.example/velvetsummitlive

Logo is available in the files below.
A series of photos have also been uploaded; please use any of these that you like throughout the design.

Menu Links from Home Page:
About Us (dropdown), Corporate Action Shows, Services (dropdown), Classes & Workshops (dropdown), The Ultimate Action Experience, Blog, Photos/Videos, Contact Us

PAGES:
- Home Page - must include a focus on Corporate Entertainment for the first glance, with information going down the page about our 4 major aspects: our Corporate Action Shows, Workshops & Classes, Services and Blog.

Required links on menu (menu does not necessarily have to be as a banner across the top - we are open to all ideas):

- Home Page

-"About Us" (dropdown with x2 pages "Our Shows" and "Our Team")

- Corporate Action Shows (x1 page)

- Services (dropdown with x3 pages "Action Showreels", and "Cosplay Competition Skits", and "Film & TV"

- Classes & Workshops (dropdown with x2 pages "Class Details & Prices" and "2016 Timetable"

- Ultimate Action Experience (x1 page with link to external website)

- Blog

- Videos & Photos or "See Us In Action" (x1 page)

- Contact Us

If you need more in-depth information into anything, please do not hesitate to send us a message!

Target Market(s)

Corporate (Classy)

Industry/Entity Type

Entertainment

Coding

Coded - Design and coding required

Number of Pages Required

5+ page

Requirements
Must have
• Website Coded via Wordpress

```html
<!DOCTYPE html>
<html lang="en">
<head>
<meta charset="utf-8">
<title>Velvet Summit Productions — Corporate Entertainment</title>
<link href="https://fonts.googleapis.com/css2?family=Source+Sans+3:wght@300;400;600;700;900&family=Open+Sans:wght@400;600&display=swap" rel="stylesheet">
<style>
:root{
  --ink:#000;
  --paper:#fff;
  --text:#2b2b2b;
  --muted:#777;
  --rule:#dcdcdc;
  --dark:#121212;
  --frame:#bdbdbd;
  --accent:#e0001b;
}
*{box-sizing:border-box;margin:0;padding:0}
html,body{width:1200px;height:2835px;overflow:hidden}
body{position:relative;background:var(--paper);font-family:"Open Sans",Arial,sans-serif;color:var(--text)}
section,header,footer{position:absolute;left:0;width:1200px}
.abs{position:absolute}

/* header */
.site-header{top:0;height:136px;background:var(--ink)}
.main-nav{position:absolute;top:18px;left:0;width:1200px;display:flex;justify-content:center;gap:22px;font-family:"Source Sans 3",sans-serif;font-size:11.5px;font-weight:600;color:var(--paper);letter-spacing:.3px}
.main-nav a{color:inherit;text-decoration:none;padding-bottom:6px}
.main-nav a.current{border-bottom:2px solid var(--paper)}
.brand{position:absolute;top:62px;left:0;width:1200px;display:flex;justify-content:center;align-items:center;gap:10px;color:var(--paper);font-family:"Source Sans 3",sans-serif;font-weight:700;font-size:22px;letter-spacing:1px;text-transform:uppercase}
.brand-mark{width:34px;height:34px;background:var(--paper)}

/* hero */
.hero{top:136px;height:548px;background:radial-gradient(ellipse at 25% 20%,#8a8a8a 0,#3d3d3d 25%,transparent 50%),radial-gradient(ellipse at 78% 18%,#7c7c7c 0,#353535 22%,transparent 48%),linear-gradient(180deg,#2a2a2a 0,#4a4a4a 55%,#2b2b2b 100%)}
.hero-title{position:absolute;top:186px;width:1200px;text-align:center;color:var(--paper);font-family:"Source Sans 3",sans-serif;line-height:1.15}
.hero-title .l1{display:block;font-weight:300;font-size:44px;letter-spacing:.5px}
.hero-title .l2{display:block;font-weight:700;font-size:34px}
.hero-dots{position:absolute;top:508px;width:1200px;display:flex;justify-content:center;gap:9px}
.hero-dots span{width:8px;height:8px;border-radius:50%;background:var(--paper)}

/* section titles */
.section-title{position:absolute;width:1200px;text-align:center;font-family:"Source Sans 3",sans-serif;font-weight:700;font-size:36px;letter-spacing:.5px;text-transform:uppercase}

/* action shows */
.shows{top:684px;height:516px;background:var(--paper)}
.shows .section-title{top:42px;color:#333}
.shows-rule{position:absolute;left:144px;top:108px;width:912px;height:1px;background:var(--rule)}
.show-card{position:absolute;top:155px;width:288px;text-align:center}
.show-photo{width:288px;height:206px;box-shadow:0 14px 12px -8px rgba(0,0,0,.45)}
.show-card h3{margin-top:22px;font-family:"Source Sans 3",sans-serif;font-weight:600;font-size:23px;color:#333}
.show-card p{margin-top:12px;font-size:12.5px;line-height:20px;color:var(--muted);padding:0 12px}
.carousel-arrow{position:absolute;top:262px}

/* classes */
.classes{top:1200px;height:588px;background:radial-gradient(ellipse at 50% 55%,#2e2e2e 0,#161616 55%,#0b0b0b 100%)}
.classes .section-title{top:62px;color:var(--paper)}
.class-item{position:absolute;top:168px;width:446px}
.class-item p{margin-top:26px;font-size:13px;line-height:23px;font-weight:600;color:var(--paper)}
.btn-outline{display:inline-block;margin-top:16px;border:1px solid var(--paper);padding:4px 10px;font-family:"Source Sans 3",sans-serif;font-size:13px;color:var(--paper);text-transform:uppercase}

/* video */
.video{position:relative;overflow:hidden}
.video-still{position:absolute;inset:0}
.play-btn{position:absolute;left:50%;top:50%;transform:translate(-50%,-50%)}
.player-bar{position:absolute;left:0;right:0;bottom:0;height:26px;background:rgba(20,20,20,.85)}
.player-bar .track{position:absolute;top:0;left:0;right:0;height:3px;background:#555}
.player-bar .played{position:absolute;top:0;left:0;height:3px;background:#999}
.player-bar .time{position:absolute;top:8px;font-size:9px;color:#ccc}
.player-bar .quality{position:absolute;top:8px;font-size:9px;color:#ccc}

/* ultimate */
.ultimate{top:1788px;height:382px;background:var(--paper)}
.ultimate h2{position:absolute;left:147px;top:64px;font-family:"Source Sans 3",sans-serif;font-weight:900;font-size:36px;line-height:42px;color:var(--ink);text-transform:uppercase}
.ultimate p{position:absolute;left:144px;top:170px;width:446px;font-size:10.5px;line-height:20px;color:#333}
.ultimate-photo{position:absolute;left:612px;top:57px;width:444px;height:279px;border:8px solid var(--frame);background:radial-gradient(ellipse at 50% 30%,#c0206a 0,#6a1044 35%,#1b0612 75%)}

/* acrobatic */
.acrobatic{top:2170px;height:525px;background:radial-gradient(ellipse at 50% 50%,#3a3a3a 0,#1a1a1a 60%,#0d0d0d 100%)}
.acrobatic .section-title{top:62px;color:var(--paper);font-size:34px}
.feature-video{position:absolute;left:223px;top:140px;width:752px;height:328px;border:5px solid var(--frame)}

/* footer */
.site-footer{top:2695px;height:140px;background:var(--paper)}
.social{position:absolute;top:26px;width:1200px;display:flex;justify-content:center;gap:8px}
.social span{width:14px;height:14px;border-radius:50%;background:#777}
.footer-nav{position:absolute;top:62px;width:1200px;display:flex;justify-content:center;font-family:"Source Sans 3",sans-serif;font-size:11px;color:#555}
.footer-nav a{color:inherit;text-decoration:none;padding:0 11px;border-left:1px solid #999}
.footer-nav a:first-child{border-left:0}
.copyright{position:absolute;top:96px;width:1200px;text-align:center;font-family:"Source Sans 3",sans-serif;font-size:10.5px;color:#555}
</style>
</head>
<body>

<header class="site-header">
  <nav class="main-nav">
    <a class="current" href="#">HOME</a>
    <a href="#">ABOUT US</a>
    <a href="#">CORPORATE ACTION SHOWS</a>
    <a href="#">SERVICES</a>
    <a href="#">CLASSES &amp; WORKSHOPS</a>
    <a href="#">THE ULTIMATE ACTION EXPERIENCE</a>
    <a href="#">BLOG</a>
    <a href="#">PHOTOS/VIDEOS</a>
    <a href="#">CONTACT US</a>
  </nav>
  <div class="brand"><span class="brand-mark"></span>Velvet Summit Productions</div>
</header>

<section class="hero" role="img" aria-label="Black and white photo of guests dancing at a corporate gala under stage spotlights">
  <h1 class="hero-title"><span class="l1">WE ARE CORPORATE ENTERTAINMENT,</span><span class="l2">ACTION &amp; ACROBATIC SHOW MAKERS.</span></h1>
  <div class="hero-dots"><span></span><span></span><span></span><span></span></div>
</section>

<section class="shows">
  <h2 class="section-title">Action Shows</h2>
  <div class="shows-rule"></div>
  <svg class="carousel-arrow" style="left:78px" width="14" height="22" viewBox="0 0 14 22"><path d="M11 2 L3 11 L11 20" fill="none" stroke="#000" stroke-width="3"/></svg>
  <svg class="carousel-arrow" style="left:1106px" width="14" height="22" viewBox="0 0 14 22"><path d="M3 2 L11 11 L3 20" fill="none" stroke="#000" stroke-width="3"/></svg>

  <article class="show-card" style="left:144px">
    <div class="show-photo" role="img" aria-label="Silhouette of a performer vaulting against a cloudy sky" style="background:linear-gradient(160deg,#dfe9e4 0,#9fb6ab 55%,#2c3a33 100%)"></div>
    <h3>Core Action Shows</h3>
    <p>See our spectacular shows "Night Raid" and "Iron Pulse"</p>
  </article>
  <article class="show-card" style="left:456px">
    <div class="show-photo" role="img" aria-label="Silhouette of an acrobat flipping off a wall at sunset" style="background:linear-gradient(180deg,#8d7d78 0,#d9a98a 55%,#4a3a33 100%)"></div>
    <h3>Core Action Shows</h3>
    <p>See our spectacular shows "Night Raid" and "Iron Pulse"</p>
  </article>
  <article class="show-card" style="left:768px">
    <div class="show-photo" role="img" aria-label="Silhouettes of two fighters sparring with staffs at sunset" style="background:radial-gradient(ellipse at 50% 75%,#f7d27a 0,#c7792a 30%,#3a2414 75%)"></div>
    <h3>Core Action Shows</h3>
    <p>See our spectacular shows "Night Raid" and "Iron Pulse"</p>
  </article>
</section>

<section class="classes" aria-label="Classes at HQ">
  <h2 class="section-title">Classes at HQ</h2>

  <div class="class-item" style="left:144px">
    <div class="video" style="width:446px;height:257px">
      <div class="video-still" role="img" aria-label="Video still of two performers fighting on stage" style="background:radial-gradient(ellipse at 50% 40%,#5a2a24 0,#2a1210 55%,#0e0606 100%)"></div>
      <svg class="play-btn" width="48" height="48" viewBox="0 0 48 48"><circle cx="24" cy="24" r="20" fill="#fff"/><circle cx="24" cy="24" r="15" fill="#111"/><path d="M19 15 L33 24 L19 33 Z" fill="#fff"/></svg>
      <div class="player-bar"><div class="track"></div><div class="played" style="width:26%"></div><span class="time" style="left:40px">0:02 / 0:10</span><span class="quality" style="right:50px">720p</span></div>
    </div>
    <p>Lorem ipsum dolor sit amet, consectetur adipiscing elit, sed do eiusmod tempor incididunt ut labore</p>
    <span class="btn-outline">Watch Video</span>
  </div>

  <div class="class-item" style="left:612px">
    <div class="video" style="width:446px;height:257px">
      <div class="video-still" role="img" aria-label="Video still of a performer in a suit doing a stunt on a wooden stage" style="background:linear-gradient(180deg,#1a1a1a 0,#2c1a12 50%,#7a3c1c 100%)"></div>
      <svg class="play-btn" width="48" height="48" viewBox="0 0 48 48"><circle cx="24" cy="24" r="20" fill="#fff"/><circle cx="24" cy="24" r="15" fill="#111"/><path d="M19 15 L33 24 L19 33 Z" fill="#fff"/></svg>
      <div class="player-bar"><div class="track"></div><div class="played" style="width:26%"></div><span class="time" style="left:40px">0:02 / 0:10</span><span class="quality" style="right:50px">720p</span></div>
    </div>
    <p>Lorem ipsum dolor sit amet, consectetur adipiscing elit, sed do eiusmod tempor incididunt ut labore</p>
    <span class="btn-outline">Watch Video</span>
  </div>
</section>

<section class="ultimate">
  <h2>The Ultimate<br>Action Experience</h2>
  <p>At vero eos et accusamus et iusto odio dignissimos ducimus qui blanditiis praesentium voluptatum deleniti atque corrupti quos dolores et quas molestias excepturi sint occaecati cupiditate non provident, similique sunt in culpa qui officia deserunt mollitia animi, id est laborum et dolorum fuga. Et harum quidem rerum facilis est et expedita distinctio. Nam libero tempore, cum soluta nobis est eligendi optio cumque nihil impedit quo minus id quod maxime placeat facere possimus, omnis voluptas assumenda</p>
  <div class="ultimate-photo" role="img" aria-label="Ballroom lit in red and purple with seated guests at a corporate event"></div>
</section>

<section class="acrobatic" aria-label="Acrobatic Action Show">
  <h2 class="section-title">Acrobatic Action Show</h2>
  <div class="feature-video video">
    <div class="video-still" role="img" aria-label="Video still of two suited performers in an acrobatic fight scene on stage" style="background:radial-gradient(ellipse at 45% 40%,#4a2620 0,#1e0e0c 55%,#080404 100%)"></div>
    <svg class="play-btn" width="64" height="64" viewBox="0 0 48 48"><circle cx="24" cy="24" r="20" fill="#fff"/><circle cx="24" cy="24" r="15" fill="#111"/><path d="M19 15 L33 24 L19 33 Z" fill="#fff"/></svg>
    <div class="player-bar" style="left:70px;right:70px;bottom:18px;height:34px">
      <div class="track" style="height:5px"></div><div class="played" style="width:25%;height:5px;background:var(--accent)"></div>
      <svg class="abs" style="left:14px;top:13px" width="10" height="12"><rect width="3" height="12" fill="#ddd"/><rect x="6" width="3" height="12" fill="#ddd"/></svg>
      <span class="time" style="left:92px;top:13px;font-size:11px">0:02 / 0:10</span>
      <span class="quality" style="right:70px;top:13px;font-size:11px">720p</span>
    </div>
  </div>
</section>

<footer class="site-footer">
  <div class="social" role="img" aria-label="Social media links"><span></span><span></span><span></span></div>
  <nav class="footer-nav">
    <a href="#">HOME</a><a href="#">ABOUT US</a><a href="#">CORPORATE ACTION SHOWS</a><a href="#">SERVICES</a><a href="#">CLASSES &amp; WORKSHOPS</a><a href="#">THE ULTIMATE ACTION EXPERIENCE</a><a href="#">BLOG</a><a href="#">PHOTOS/VIDEOS</a><a href="#">CONTACT US</a>
  </nav>
  <div class="copyright">© 2016 COMPANY NAME &nbsp;|&nbsp; ALL RIGHTS RESERVED</div>
</footer>

</body>
</html>
```